Business Card Design

We need a new business card design for a CPA office that has been in business for over 10 years. We are a Accounting Concierge firm that offers the following services: Certified Public Accountant, Personal & Business Tax Preparation, Accounting, Bookkeeping, Payroll Services, Tax Litigation Services.
Certified LedgerNest CertPartner.  We would like to see designs that use the color navy blue in the company logo with classic accent colors.  We would like the card to be on a textured high pound card stock and that is more classic and less modern in design.  The final design should communicate class and professionalism.

Reason: I gave feedback to many of the designers with some changes.  Please re-read the brief as we would like to remove the photo of the man on the card.  We also want only light grey or white background, not navy or blue - the navy or blue tones should be the font or accent colors.  Please also, consider creating a logo with the initials P&W or PW or P&W CPA.

Industry/Entity Type
Business
Contact Information for Business Card
Pellford & Company CPA, Dominic Pellford III, 4317 Larkmoor Road, Suite D, Bradenton, FL  34519, Phone: (941) 555-0137, Fax: (941) 555-0182, Email: Dominic@DPellfordCPA.example, Website: www.DPellfordCPA.example
Requirements
Must have
- LedgerNest Logo

Should not have
- we no longer want the photo on the card.

```html
<!DOCTYPE html>
<html lang="en">
<head>
<meta charset="utf-8">
<title>Pellford &amp; Company CPA — Business Card</title>
<link rel="stylesheet" href="https://fonts.googleapis.com/css2?family=Catamaran:wght@400;500;600&family=Open+Sans:wght@400;600&display=swap">
<style>
  :root {
    --paper: #ffffff;
    --frame-red: #d9161c;
    --navy: #0b0b8a;
    --sky: #3db7ea;
    --ink: #222222;
    --badge-yellow: #f8d416;
  }
  html, body {
    margin: 0;
    padding: 0;
    width: 1200px;
    height: 702px;
    overflow: hidden;
    background: var(--paper);
  }
  .card {
    position: relative;
    width: 1200px;
    height: 702px;
    background: var(--paper);
    font-family: "Catamaran", "Open Sans", sans-serif;
  }
  .card-frame {
    position: absolute;
    left: 22px;
    top: 22px;
    width: 1150px;
    height: 652px;
    border: 4px solid var(--frame-red);
  }
  .contact-top {
    position: absolute;
    right: 78px;
    top: 70px;
    text-align: right;
  }
  .contact-phones {
    font-size: 30px;
    font-weight: 600;
    color: var(--ink);
    line-height: 40px;
    letter-spacing: 0.3px;
  }
  .contact-email {
    font-size: 27px;
    font-weight: 400;
    color: var(--ink);
    line-height: 40px;
  }
  .link { color: var(--sky); }
  .firm-name {
    position: absolute;
    left: 0;
    width: 1156px;
    top: 225px;
    margin: 0;
    text-align: center;
    font-family: "Open Sans", sans-serif;
    font-weight: 600;
    font-size: 46px;
    color: var(--navy);
    letter-spacing: 0.5px;
    line-height: 56px;
  }
  .firm-tagline {
    position: absolute;
    left: 0;
    width: 1172px;
    top: 280px;
    margin: 0;
    text-align: center;
    font-family: "Open Sans", sans-serif;
    font-size: 31px;
    color: var(--sky);
    line-height: 40px;
  }
  .divider {
    position: absolute;
    left: 222px;
    top: 337px;
    width: 714px;
    border-top: 2px dotted var(--ink);
  }
  .services {
    position: absolute;
    left: 0;
    width: 1174px;
    top: 356px;
    margin: 0;
    text-align: center;
    font-family: "Open Sans", sans-serif;
    font-size: 27px;
    color: var(--navy);
    line-height: 38px;
  }
  .services .sep { color: var(--sky); margin: 0 12px; }
  .address-block {
    position: absolute;
    left: 70px;
    top: 490px;
    font-size: 28px;
    color: var(--ink);
    line-height: 36px;
  }
  .address-block .indent { padding-left: 44px; }
  .address-block .label-a { padding-left: 14px; }
  .address-block .web { margin-top: 2px; }
  .cert-badge {
    position: absolute;
    left: 952px;
    top: 497px;
  }
</style>
</head>
<body>
<div class="card">
  <div class="card-frame"></div>

  <div class="contact-top">
    <div class="contact-phones">M: (941) 555-0137&nbsp; F: (941) 555-0182</div>
    <div class="contact-email">E: <span class="link">Dominic@DPellfordCPA.example</span></div>
  </div>

  <h1 class="firm-name">PELLFORD &amp; COMPANY CPA, LLC</h1>
  <p class="firm-tagline">Full Service Tax and Accounting</p>
  <div class="divider"></div>

  <p class="services">
    Certified Public Accountant<span class="sep">/</span>Personal &amp; Business Tax&nbsp; Preparation<br>
    Bookkeeping<span class="sep">/</span>Accounting<span class="sep">/</span>Payroll Services<span class="sep">/</span>Tax Litigation Services
  </p>

  <div class="address-block">
    <div class="label-a">A: Pellford &amp; Company CPA, Dominic Pellford</div>
    <div class="indent">4317 Larkmoor Road, Suite D, Bradenton,</div>
    <div class="indent">FL 34519,</div>
    <div class="web">W: <span class="link">www.DPellfordCPA.example</span></div>
  </div>

  <svg class="cert-badge" width="140" height="140" viewBox="0 0 140 140" role="img" aria-label="LedgerNest CertPartner certification badge">
    <circle cx="70" cy="70" r="66" fill="var(--badge-yellow)"/>
  </svg>
</div>
</body>
</html>
```